Modern Quillby Tree Care Website

I need a website for a full service Tree Care company. The company provides tree pruning, tree removal, tree preservation, emergency services, stump grinding, and emergency tree services.

Target Market(s)

Customers that need tree services

Industry/Entity Type

Landscaping, Tree Services

Coding

Coded - Design and coding required

Number of Pages Required

5+ page

Font styles to use
Sans Serif

Requirements
Must have
• Good clean design that showcases the services the company provides.
Nice to have
• Services page; contact form, blog, home page, about page

```html
<!DOCTYPE html>
<html lang="en">
<head>
<meta charset="utf-8">
<title>Quillby Tree Care</title>
<link href="https://fonts.googleapis.com/css2?family=Inter:wght@400;500;600;700;800&display=swap" rel="stylesheet">
<style>
:root{
  --forest:#2f4a25;
  --forest-deep:#1e2a1a;
  --amber:#f5a623;
  --lime:#e4ea78;
  --cream:#f4f3d3;
  --ink:#1c1c1c;
  --muted:#555;
  --white:#fff;
  --line:#c9c9c9;
}
*{box-sizing:border-box;margin:0;padding:0}
html,body{width:1200px;height:3643px;overflow:hidden}
body{font-family:'Inter',sans-serif;color:var(--ink);background:var(--white);position:relative}
.abs{position:absolute}
.brand{display:flex;align-items:center;gap:16px;font-weight:800;font-size:38px;letter-spacing:1px;white-space:nowrap}
.brand-mark{width:40px;height:40px;background:var(--amber);flex:none}
.site-header .brand{left:90px;top:74px;color:var(--forest)}
.menu-toggle{left:1020px;top:86px;width:64px}
.menu-toggle span{display:block;height:6px;background:var(--ink);border-radius:3px;margin-bottom:12px}
.hero-title{left:123px;top:236px;font-size:44px;line-height:58px;font-weight:800;color:var(--forest)}
.hero-title em{font-style:normal;color:var(--amber)}
.hero-sub{left:126px;top:362px;width:500px;font-size:16px;line-height:22px;font-weight:600}
.btn{display:inline-flex;align-items:center;justify-content:center;border-radius:30px;font-weight:600;font-size:16px;white-space:nowrap}
.btn-dark{background:var(--forest);color:var(--white)}
.btn-outline{border:2px solid var(--forest);color:var(--forest);background:var(--white)}
.btn-cream{background:var(--cream);color:var(--forest)}
.btn-white-outline{border:2px solid var(--forest);color:var(--forest);background:var(--white)}
.photo{border-radius:14px}
.green-band{left:0;top:0;width:1200px;height:1060px}
.intro-heading{left:520px;top:712px;font-size:26px;font-weight:700;color:var(--lime)}
.intro-tag{left:520px;top:750px;font-size:16px;font-weight:600;color:var(--white)}
.intro-body{left:520px;top:786px;width:560px;font-size:12px;line-height:17px;color:#e8eee4}
.service-kicker{left:183px;top:1158px;font-size:15px;color:#7cac2c;font-weight:600}
.service-title{left:183px;top:1183px;font-size:30px;font-weight:700;color:var(--forest)}
.service-body{left:183px;top:1230px;width:400px;font-size:12px;line-height:17px;color:var(--muted)}
.features{left:0;top:1493px;width:1200px;height:174px;background:var(--forest);display:flex;justify-content:center;gap:62px;padding-top:22px}
.feature{width:96px;text-align:center;color:var(--white);font-size:13px;line-height:16px;font-weight:500}
.feature svg{display:block;margin:0 auto 8px}
.section-title{width:1200px;text-align:center;font-weight:700}
.card{left:133px;top:1920px;width:934px;height:357px;background:var(--white);border:2px solid #ddd;border-radius:22px;box-shadow:0 12px 22px rgba(0,0,0,.28)}
.quote{left:74px;top:60px;width:760px;font-size:21px;line-height:31px}
.read-more{left:74px;top:154px;font-size:16px;color:var(--muted)}
.stars{left:666px;top:166px;display:flex;gap:8px}
.avatar{left:74px;top:218px;width:84px;height:84px;border-radius:50%;background:linear-gradient(160deg,#7ec8c6,#3c8a88)}
.reviewer{left:196px;top:246px;font-size:21px;font-weight:600}
.consult{left:0;top:2417px;width:1200px;height:676px;background:var(--forest)}
.consult h2{left:133px;top:62px;font-size:27px;font-weight:700;color:var(--white)}
.consult p{left:133px;top:108px;width:760px;font-size:19px;line-height:25px;color:#eef2ea}
.field{background:var(--white);border:2px solid var(--line);border-radius:12px;color:#aaa;font-size:17px;padding:16px 20px}
.site-footer{left:0;top:3250px;width:1200px;height:393px;background:var(--forest-deep);color:var(--white)}
.site-footer .brand{left:100px;top:100px;color:var(--white);font-size:24px;gap:14px}
.site-footer .brand-mark{width:36px;height:36px}
.socials{left:100px;top:225px;display:flex;gap:26px}
.socials span{width:52px;height:52px;border-radius:50%;background:var(--cream)}
.col-title{font-size:24px;font-weight:700;color:var(--amber)}
.contact-line{display:flex;align-items:center;gap:24px;font-size:17px;font-weight:600}
.menu-list{list-style:none;font-size:18px;line-height:36px;font-weight:500}
.divider{left:100px;top:315px;width:1000px;height:1px;background:#7a8275}
.copyright{left:0;top:342px;width:1200px;text-align:center;font-size:17px}
</style>
</head>
<body>

<header class="site-header">
  <div class="abs brand"><span class="brand-mark"></span>QUILLBY</div>
  <div class="abs menu-toggle" aria-label="Menu"><span></span><span></span><span></span></div>
</header>

<svg class="abs green-band" viewBox="0 0 1200 1060" aria-hidden="true">
  <path d="M0 632 C 350 665, 800 640, 1200 495 L1200 1060 L0 1060 Z" fill="var(--forest)"/>
</svg>

<section class="hero">
  <h1 class="abs hero-title">Call <em>QUILLBY</em> For All Your<br>Tree Care Needs</h1>
  <p class="abs hero-sub">Discover Quillby, Your Reliable Choice for All Your Tree Care Essentials, Ensuring Your Greenery Thrives.</p>
  <a class="abs btn btn-dark" style="left:128px;top:440px;width:212px;height:48px">
    <svg width="18" height="18" viewBox="0 0 24 24" style="margin-right:12px"><path d="M6.6 10.8a15 15 0 0 0 6.6 6.6l2.2-2.2a1 1 0 0 1 1-.25 11.4 11.4 0 0 0 3.6.57 1 1 0 0 1 1 1V20a1 1 0 0 1-1 1A17 17 0 0 1 3 4a1 1 0 0 1 1-1h3.5a1 1 0 0 1 1 1c0 1.25.2 2.45.57 3.57a1 1 0 0 1-.25 1Z" fill="#fff"/></svg>(333) 555-0147</a>
  <a class="abs btn btn-outline" style="left:357px;top:440px;width:210px;height:48px">Explore Quillby</a>
  <svg class="abs" style="left:700px;top:150px" width="350" height="350" viewBox="0 0 350 350" aria-hidden="true">
    <path d="M50 110 A150 150 0 1 0 300 95" fill="none" stroke="#3f7d2a" stroke-width="10" stroke-linecap="round"/>
  </svg>
  <div class="abs" role="img" aria-label="Boardwalk path through a lush green forest" style="left:720px;top:160px;width:310px;height:310px;border-radius:50%;background:radial-gradient(circle at 50% 40%,#9bbd76,#41632d 70%,#2a3f1f)"></div>
</section>

<section class="intro">
  <div class="abs photo" role="img" aria-label="Volunteers planting a young tree" style="left:157px;top:693px;width:303px;height:180px;background:linear-gradient(135deg,#7a9a52,#4a6a30 60%,#8c6d4c)"></div>
  <div class="abs photo" role="img" aria-label="Gloved hands in soil" style="left:157px;top:880px;width:98px;height:93px;background:linear-gradient(135deg,#8aa75a,#5a3f2a)"></div>
  <div class="abs photo" role="img" aria-label="Crew tending garden trees" style="left:260px;top:880px;width:98px;height:93px;background:linear-gradient(135deg,#5f8a3e,#a54c3c)"></div>
  <div class="abs photo" role="img" aria-label="Planting a sapling" style="left:363px;top:880px;width:97px;height:93px;background:linear-gradient(135deg,#9fbd6d,#4e6e34)"></div>
  <h2 class="abs intro-heading">Introducing QUILLBY</h2>
  <p class="abs intro-tag">Our Ultimate Destination for Exceptional Tree Care Services</p>
  <p class="abs intro-body">At Quillby Tree Care, we are more than just a tree service company; we are stewards of our beautiful trees. With a passion deeply rooted in arboriculture, we dedicate ourselves to promote the health, beauty, and safety of your trees and landscapes. Whether it's expert tree trimming to enhance aesthetics, careful tree removal to reduce hazards, or complete tree health checks to ensure safety, we approach each task with unwavering dedication and attention to detail.</p>
  <a class="abs btn btn-cream" style="left:520px;top:900px;width:130px;height:36px;font-size:12px">Read More</a>
</section>

<section class="services">
  <p class="abs service-kicker">Choose Your Tree Care Services</p>
  <h2 class="abs service-title">Tree Triming</h2>
  <p class="abs service-body">Lorem ipsum dolor sit amet, consectetur adipiscing elit, sed do eiusmod tempor incididunt ut labore et dolore magna aliqua. Ut enim ad minim veniam, quis nostrud exercitation ullamco laboris nisi ut aliquip ex ea commodo consequat. Duis aute irure dolor in reprehenderit in voluptate velit esse cillum dolore eu fugiat nulla pariatur. Excepteur sint occaecat cupidatat non proident.</p>
  <a class="abs btn btn-dark" style="left:183px;top:1365px;width:140px;height:34px;font-size:12px">Service Detail</a>
  <a class="abs btn btn-white-outline" style="left:332px;top:1365px;width:130px;height:34px;font-size:12px">Book Service</a>
  <div class="abs" role="img" aria-label="Arborist working in a tree" style="left:653px;top:1190px;width:90px;height:205px;border-radius:12px 0 0 12px;background:linear-gradient(160deg,#7aa36a,#3d5a30)"></div>
  <div class="abs" role="img" aria-label="Arborist cutting a trunk with a chainsaw" style="left:733px;top:1143px;width:245px;height:297px;border-radius:14px;background:linear-gradient(160deg,#cfd9e2,#8a6f54 55%,#2f3d2a);box-shadow:0 6px 14px rgba(0,0,0,.3)"></div>
  <div class="abs" role="img" aria-label="Climber pruning branches" style="left:968px;top:1190px;width:82px;height:205px;border-radius:0 12px 12px 0;background:linear-gradient(160deg,#d6b27a,#6c8a4a)"></div>
</section>

<section class="abs features">
  <div class="feature"><svg width="64" height="64" viewBox="0 0 64 64" fill="none" stroke="#fff" stroke-width="2.5"><rect x="14" y="10" width="30" height="40" rx="3"/><path d="M20 20h18M20 28h18M20 36h10"/><circle cx="44" cy="44" r="8"/><path d="M40 44l3 3 5-6"/></svg>Licensed and Insured</div>
  <div class="feature"><svg width="64" height="64" viewBox="0 0 64 64" fill="none" stroke="#fff" stroke-width="2.5"><circle cx="32" cy="32" r="22"/><text x="32" y="37" text-anchor="middle" font-size="13" font-family="Inter,sans-serif" fill="#fff" stroke="none" font-weight="700">24/7</text></svg>24 Hours Emergency Services</div>
  <div class="feature"><svg width="64" height="64" viewBox="0 0 64 64" fill="none" stroke="#fff" stroke-width="2.5"><path d="M10 30L32 12l22 18"/><path d="M16 26v26h32V26"/><rect x="27" y="38" width="10" height="14"/></svg>Locally Owned and Operated</div>
  <div class="feature"><svg width="64" height="64" viewBox="0 0 64 64" fill="none" stroke="#fff" stroke-width="2.5"><circle cx="32" cy="18" r="7"/><path d="M20 44c0-8 5-14 12-14s12 6 12 14"/><circle cx="14" cy="28" r="5"/><circle cx="50" cy="28" r="5"/><path d="M6 48c0-6 3-10 8-10M58 48c0-6-3-10-8-10"/></svg>Professional Work</div>
  <div class="feature"><svg width="64" height="64" viewBox="0 0 64 64" fill="none" stroke="#fff" stroke-width="2.5"><path d="M32 8l20 8v14c0 13-9 22-20 26-11-4-20-13-20-26V16z"/><path d="M24 32l6 6 11-12"/></svg>Safety is Our No 1 Priority</div>
  <div class="feature"><svg width="64" height="64" viewBox="0 0 64 64" fill="none" stroke="#fff" stroke-width="2.5"><circle cx="28" cy="32" r="16"/><path d="M28 24v16M24 28h6a3 3 0 0 1 0 6h-4a3 3 0 0 0 0 6h6"/><path d="M46 18l8-4M48 30h8"/></svg>Free Estimates</div>
</section>

<section class="testimonials">
  <h2 class="abs section-title" style="left:0;top:1775px;font-size:26px">What Client Say About Us</h2>
  <p class="abs section-title" style="left:0;top:1823px;font-size:22px;line-height:30px;font-weight:400">Lorem ipsum dolor sit amet, consectetur adipiscing elit, sed do eiusmod tempor<br>incididunt ut labore et dolore magna aliqua.</p>
  <article class="abs card">
    <p class="abs quote">Lorem ipsum dolor sit amet, consectetur adipiscing elit, sed do eiusmod tempor incididunt ut labore et dolore magna aliqua.</p>
    <p class="abs read-more">ReadMore</p>
    <div class="abs stars">
      <svg width="36" height="36" viewBox="0 0 24 24"><path d="M12 2l3 6.5 7 .8-5.2 4.8 1.4 7L12 17.6 5.8 21l1.4-7L2 9.3l7-.8z" fill="var(--amber)"/></svg>
      <svg width="36" height="36" viewBox="0 0 24 24"><path d="M12 2l3 6.5 7 .8-5.2 4.8 1.4 7L12 17.6 5.8 21l1.4-7L2 9.3l7-.8z" fill="var(--amber)"/></svg>
      <svg width="36" height="36" viewBox="0 0 24 24"><path d="M12 2l3 6.5 7 .8-5.2 4.8 1.4 7L12 17.6 5.8 21l1.4-7L2 9.3l7-.8z" fill="var(--amber)"/></svg>
      <svg width="36" height="36" viewBox="0 0 24 24"><path d="M12 2l3 6.5 7 .8-5.2 4.8 1.4 7L12 17.6 5.8 21l1.4-7L2 9.3l7-.8z" fill="var(--amber)"/></svg>
      <svg width="36" height="36" viewBox="0 0 24 24"><path d="M12 2l3 6.5 7 .8-5.2 4.8 1.4 7L12 17.6 5.8 21l1.4-7L2 9.3l7-.8z" fill="var(--amber)"/></svg>
    </div>
    <div class="abs avatar" role="img" aria-label="Portrait of the reviewer"></div>
    <p class="abs reviewer">Marla Teversham</p>
  </article>
  <svg class="abs" style="left:905px;top:2296px" width="170" height="30" viewBox="0 0 170 30" fill="none" stroke="#bbb" stroke-width="2.5">
    <path d="M72 15H4M14 6L4 15l10 9"/><path d="M98 15h68M156 6l10 9-10 9"/>
  </svg>
</section>

<section class="abs consult">
  <h2 class="abs">Seek For Expert Advice Consulting</h2>
  <p class="abs">Lorem ipsum dolor sit amet, consectetur adipiscing elit, sed do eiusmod tempor incididunt ut labore et dolore magna aliqua.</p>
  <div class="abs field" style="left:140px;top:210px;width:460px;height:56px">First Name</div>
  <div class="abs field" style="left:633px;top:210px;width:434px;height:56px">Last Name</div>
  <div class="abs field" style="left:140px;top:294px;width:460px;height:56px">Email Address</div>
  <div class="abs field" style="left:633px;top:294px;width:434px;height:56px">Phone</div>
  <div class="abs field" style="left:140px;top:376px;width:927px;height:146px">Messages</div>
  <a class="abs btn btn-cream" style="left:843px;top:550px;width:224px;height:58px;border-radius:10px;font-weight:500;color:var(--ink)">Submit</a>
</section>

<footer class="abs site-footer">
  <div class="abs brand"><span class="brand-mark" style="background:var(--white)"></span>QUILLBY TREE CARE</div>
  <div class="abs socials" aria-label="Social links"><span></span><span></span><span></span><span></span></div>
  <h3 class="abs col-title" style="left:487px;top:62px">Contact Me</h3>
  <p class="abs contact-line" style="left:487px;top:122px">
    <svg width="36" height="36" viewBox="0 0 24 24"><path d="M6.6 10.8a15 15 0 0 0 6.6 6.6l2.2-2.2a1 1 0 0 1 1-.25 11.4 11.4 0 0 0 3.6.57 1 1 0 0 1 1 1V20a1 1 0 0 1-1 1A17 17 0 0 1 3 4a1 1 0 0 1 1-1h3.5a1 1 0 0 1 1 1c0 1.25.2 2.45.57 3.57a1 1 0 0 1-.25 1Z" fill="#fff"/></svg>(333) 555-0147</p>
  <p class="abs contact-line" style="left:487px;top:188px">
    <svg width="36" height="36" viewBox="0 0 24 24" fill="none" stroke="#fff" stroke-width="2"><rect x="3" y="5" width="18" height="14" rx="1"/><path d="M3 6l9 7 9-7"/></svg>hello @ quillbymail.com</p>
  <h3 class="abs col-title" style="left:827px;top:62px">Menu</h3>
  <ul class="abs menu-list" style="left:827px;top:112px">
    <li>Home</li><li>About</li><li>Tree Care Services</li><li>Expert Advice &amp; Consulting</li>
  </ul>
  <div class="abs divider"></div>
  <p class="abs copyright">Copyright © 2024 | Quillby Tree Care | All rights reserved.</p>
</footer>

</body>
</html>
```